We require a professional design for a Cosmetic Surgery college. We have just submitted the request for our new logo which will be used on this card. We are the leaders in our field of education in Australia and this should be reflected in the quality of the card. People want to come and study with us because we are so outstanding in the field. Studying with us provides credibility, quality and courage.
Updates

Project Deadline Extended
Reason: Require updated logo to be used in design

Target Market(s)

25 - 40 year old professional women primarily from a medical background wanting to continue study in the cosmetic medical field, western speaking countries. The course average cost is 17k AU for 16 weeks.

Industry/Entity Type

Education

Requirements
Must have
• Must us the logo that is currently under design by this company.
Nice to have
• A medical twist very subtle would be nice possilbly rod of Asclepius.
Should not have
• Should not look old, we are dealing with modern medical concepts.
The logo that is being redesigned 3d silver, the attached logo is the old one.

```html
<!DOCTYPE html>
<html lang="en">
<head>
<meta charset="utf-8">
<title>Ashmere Business Card</title>
<link rel="stylesheet" href="https://fonts.googleapis.com/css2?family=Open+Sans:wght@400;600&display=swap">
<style>
  :root {
    --backdrop: #d9d9d9;
    --card-dark: #1f1c1d;
    --card-light: #ffffff;
    --ink: #2a2728;
    --silver: #a9a9ab;
    --silver-light: #cfcfd1;
    --band: #1c1a1b;
  }
  * { margin: 0; padding: 0; box-sizing: border-box; }
  html, body {
    width: 1200px; height: 676px; overflow: hidden;
    background: var(--backdrop);
    font-family: "Open Sans", Arial, sans-serif;
  }
  .stage {
    width: 1200px; height: 676px;
    display: flex; align-items: center; justify-content: center; gap: 60px;
  }
  .card {
    position: relative;
    width: 520px; height: 298px;
    overflow: hidden;
    box-shadow: 0 6px 18px rgba(0,0,0,.25);
  }
  .card--front { background: var(--card-dark); }
  .card--back { background: var(--card-light); }

  .brand {
    position: absolute;
    display: flex; align-items: center; gap: 12px;
    font-family: "Open Sans", Arial, sans-serif;
    font-weight: 600;
    letter-spacing: 3px;
    color: var(--silver);
  }
  .brand__dot {
    width: 34px; height: 34px; border-radius: 50%;
    background: var(--silver);
  }
  .card--front .brand { left: 52px; top: 124px; font-size: 40px; }
  .card--back .brand { right: 40px; top: 40px; font-size: 34px; }
  .card--back .brand__dot { width: 30px; height: 30px; }

  .name-band {
    position: absolute; left: 0; top: 104px;
    width: 100%; height: 28px;
    background: var(--band);
    color: #fff;
    display: flex; align-items: center; padding-left: 30px;
    font-size: 15px;
  }
  .name-band__role { font-size: 11px; color: var(--silver-light); margin-left: 8px; padding-left: 8px; border-left: 1px solid var(--silver-light); }

  .contacts {
    position: absolute; left: 30px; top: 142px;
    list-style: none;
    font-size: 11.5px; color: var(--ink); line-height: 17px;
  }
  .contacts li { display: flex; align-items: center; gap: 8px; }
  .contacts svg { width: 9px; height: 9px; fill: var(--ink); }

  .address {
    position: absolute; right: 40px; top: 180px;
    text-align: right;
    font-size: 11.5px; color: var(--ink); line-height: 16px;
    display: flex; align-items: center; gap: 8px;
  }
  .address svg { width: 10px; height: 13px; fill: var(--ink); }

  .swoosh { position: absolute; left: 0; bottom: 0; width: 520px; height: 74px; }
</style>
</head>
<body>
<main class="stage">
  <section class="card card--front" aria-label="Card front">
    <div class="brand"><span class="brand__dot"></span>ASHMERE</div>
  </section>

  <section class="card card--back" aria-label="Card back">
    <div class="brand"><span class="brand__dot"></span>ASHMERE</div>

    <div class="name-band">your name<span class="name-band__role">designation</span></div>

    <ul class="contacts">
      <li><svg viewBox="0 0 10 10"><rect x="2" y="0" width="6" height="10" rx="1"/></svg>0123 456 789</li>
      <li><svg viewBox="0 0 10 10"><rect x="0.5" y="0.5" width="9" height="9" fill="none" stroke="#2a2728"/></svg>0123 456 789</li>
      <li><svg viewBox="0 0 10 10"><rect x="0" y="2" width="10" height="7"/></svg>youremail@mail.com</li>
      <li><svg viewBox="0 0 10 10"><circle cx="5" cy="5" r="4.5"/></svg>www.yourwebsite.com</li>
    </ul>

    <div class="address">
      <span>address (street address<br>suite number, city, state, zip</span>
      <svg viewBox="0 0 10 13"><path d="M5 0a5 5 0 0 1 5 5c0 3-5 8-5 8S0 8 0 5a5 5 0 0 1 5-5z"/></svg>
    </div>

    <svg class="swoosh" viewBox="0 0 520 74" preserveAspectRatio="none" aria-hidden="true">
      <path d="M0 0 C60 26 160 40 300 48 C400 54 470 62 520 74 L0 74 Z" fill="var(--band)"/>
      <path d="M0 18 C120 50 300 46 420 56 C470 61 500 67 520 73" fill="none" stroke="var(--silver)" stroke-width="5"/>
      <path d="M0 32 C140 62 320 56 440 64 C480 67 505 70 520 74" fill="none" stroke="var(--card-light)" stroke-width="2.5"/>
    </svg>
  </section>
</main>
</body>
</html>
```